New Packaging Design Project

Wine packaging redesign. Retail partner requested a redesign of a private label wine. The old label is attached. Our partner liked the Copper Wren Hollow label and wanted something similar. There will be a logo added to the top of the label

Went on vacation/holiday

```html
<!DOCTYPE html>
<html lang="en">
<head>
<meta charset="utf-8">
<title>Napa Valey Red Blend 2018 – Wine Label</title>
<link rel="stylesheet" href="https://fonts.googleapis.com/css2?family=Yanone+Kaffeesatz:wght@400;500;700&display=swap">
<style>
  :root {
    --page-white: #ffffff;
    --stage-light: #fbfbfb;
    --stage-edge: #ececec;
    --band-grey: #e6e6e6;
    --label-grey: #6b6967;
    --teal: #7fd8d1;
    --pink: #d46a98;
  }
  html, body {
    margin: 0;
    padding: 0;
    width: 1200px;
    height: 1000px;
    overflow: hidden;
    background: var(--page-white);
  }
  .canvas {
    position: relative;
    width: 1200px;
    height: 1000px;
    font-family: "Yanone Kaffeesatz", "Arial Narrow", sans-serif;
  }
  .stage {
    position: absolute;
    left: 0;
    top: 161px;
    width: 1200px;
    height: 694px;
    background: radial-gradient(ellipse at center, var(--stage-light) 40%, var(--stage-edge) 100%);
  }
  .stage-band {
    position: absolute;
    left: 0;
    width: 1200px;
    background: var(--band-grey);
  }
  .stage-band--top { top: 0; height: 27px; }
  .stage-band--bottom { bottom: 0; height: 32px; }
  .wine-label {
    position: absolute;
    left: 382px;
    top: 282px;
    width: 478px;
    height: 472px;
    background: var(--label-grey);
    text-align: center;
  }
  .region-title {
    position: absolute;
    left: 0;
    right: 0;
    top: 66px;
    margin: 0;
    font-weight: 700;
    font-size: 66px;
    line-height: 1;
    letter-spacing: 0.5px;
    color: var(--teal);
  }
  .vineyard-art {
    position: absolute;
    left: 96px;
    top: 168px;
    width: 286px;
    height: 162px;
    background: linear-gradient(180deg, rgba(212,106,152,0.55) 0%, rgba(212,106,152,0.35) 25%, rgba(127,216,209,0.3) 60%, rgba(212,106,152,0.25) 100%);
    border-radius: 4px;
  }
  .blend-name {
    position: absolute;
    left: 0;
    right: 0;
    top: 347px;
    margin: 0;
    font-weight: 700;
    font-size: 19px;
    letter-spacing: 1.5px;
    color: var(--pink);
  }
  .grape-list {
    position: absolute;
    left: 0;
    right: 0;
    margin: 0;
    font-weight: 400;
    font-size: 13px;
    letter-spacing: 0.4px;
    color: var(--teal);
    word-spacing: 2px;
  }
  .grape-list--first { top: 375px; }
  .grape-list--second { top: 392px; }
  .grape-list .divider { padding: 0 18px; }
  .vintage {
    position: absolute;
    left: 0;
    right: 0;
    top: 412px;
    margin: 0;
    font-weight: 700;
    font-size: 20px;
    letter-spacing: 1px;
    color: var(--pink);
  }
</style>
</head>
<body>
  <div class="canvas">
    <div class="stage">
      <div class="stage-band stage-band--top"></div>
      <div class="stage-band stage-band--bottom"></div>
    </div>

    <section class="wine-label">
      <h1 class="region-title">NAPA VALEY</h1>
      <div class="vineyard-art" role="img" aria-label="Line illustration of a pink hill above rolling vineyard rows in pink and teal"></div>
      <h2 class="blend-name">RED BLEND</h2>
      <p class="grape-list grape-list--first">MERLOT<span class="divider">|</span>CABERNET SAUVIGNON</p>
      <p class="grape-list grape-list--second">CABERNET FRANC<span class="divider">|</span>PETIT VERDOT<span class="divider">|</span>MALBEC</p>
      <p class="vintage">2018</p>
    </section>
  </div>
</body>
</html>
```